BrightWave Tristate Commercial Cleaning Brochure

We need a tri fold brochure that we can use to market our commercial cleaning services to clients. We are looking for something that will stand out. We don't want to use any faces of people on the brochures, only cleaning tools and supplies. We offer Office Cleaning, Covid Cleaning, Janitorial and Floor Services

Target Market(s)

Small to large businesses

Industry/Entity Type

Commercial Cleaning

Colors
0054AA
0677BA
7BADD7
CADEEF
E8F1F8
0094D4
00A9DD
6FCCEA
C7EBF8
E9F6FB
00AB8E
00BBA5
67D7C9
C6EFE9
E9F9F6
59FF00
82FF00
B8FF75
E3FFCB
F4FFEA

Requirements
Must have
• Stand out design-Eye Catching
Should not have
• faces of ppl the brochure

```html
<!DOCTYPE html>
<html lang="en">
<head>
<meta charset="utf-8">
<title>BrightWave Tristate – Commercial Cleaning Brochure</title>
<link href="https://fonts.googleapis.com/css2?family=Quicksand:wght@500;600;700&display=swap" rel="stylesheet">
<style>
  :root{
    --bg:#ffffff;
    --green:#5c9b2f;
    --green-light:#7cc242;
    --blue:#1d4f9e;
    --ink:#2b2b2b;
    --white:#ffffff;
    --paper-shadow:rgba(0,0,0,.22);
  }
  *{box-sizing:border-box;margin:0;padding:0}
  html,body{width:800px;height:1200px;overflow:hidden;background:var(--bg)}
  body{position:relative;font-family:"Quicksand",sans-serif;color:var(--ink)}
  .sheet{position:absolute;left:40px;width:720px;height:509px;background:var(--white);
    box-shadow:0 4px 14px var(--paper-shadow);overflow:hidden}
  .sheet--outside{top:48px}
  .sheet--inside{top:630px}
  .sheet svg.art{position:absolute;left:0;top:0;width:720px;height:509px}
  .heading{position:absolute;font-weight:600;font-size:20px;line-height:1;white-space:nowrap}
  .heading .accent{color:var(--green)}
  .heading .main{color:var(--blue)}
  .heading::after{content:"";display:block;width:28px;height:2px;background:var(--ink);margin-top:6px}
  .copy{position:absolute;width:188px;font-size:6.6px;line-height:1.45;font-weight:500;color:var(--ink)}
  .copy p+p{margin-top:9px}
  .review-title{position:absolute;left:26px;top:356px;color:var(--white);font-size:19px;font-weight:600}
  .review-title::after{content:"";display:block;width:26px;height:2px;background:var(--white);margin-top:7px}
  .quote-box{position:absolute;left:26px;top:398px;width:188px;height:92px;border:1.5px solid var(--white);
    border-radius:6px;padding:20px 12px 8px;color:var(--white);font-size:6.4px;line-height:1.45}
  .quote-box .mark{position:absolute;left:10px;top:-8px;font-size:26px;line-height:1;background:var(--green);padding:0 3px}
  .quote-box .by{display:block;text-align:right;margin-top:5px}
  .quote-box .by::before{content:"";display:inline-block;width:24px;height:1px;background:var(--white);vertical-align:middle;margin-right:3px}
  .contact-title{position:absolute;left:266px;top:402px;color:var(--white);font-size:19px;font-weight:600}
  .contact-title::after{content:"";display:block;width:26px;height:2px;background:var(--white);margin-top:7px}
  .contact-list{position:absolute;left:266px;top:440px;list-style:none;color:var(--white);font-size:8px;font-weight:600}
  .contact-list li{display:flex;align-items:center;gap:4px;height:20px}
  .contact-list svg{width:8px;height:8px;fill:var(--white)}
  .cover-title{position:absolute;left:480px;top:405px;width:240px;text-align:center;color:var(--white);
    font-size:22px;font-weight:500;line-height:1.1}
  .cover-title::after{content:"";display:block;width:186px;height:1.5px;background:var(--white);margin:8px auto 0}
  .cover-url{position:absolute;left:480px;top:472px;width:240px;text-align:center;color:var(--white);font-size:11px;letter-spacing:.6px;font-weight:600}
  .brand{position:absolute;color:var(--blue);font-weight:700;line-height:1;text-align:center;white-space:nowrap}
  .brand--cover{left:520px;top:44px;width:200px;font-size:24px}
  .brand--cover small{display:block;font-size:13px;margin-top:2px}
  .brand--badge{left:272px;top:320px;width:92px;font-size:12.5px}
  .brand--badge small{display:block;font-size:7px;margin-top:1px}
</style>
</head>
<body>

<!-- Outside spread: floor services / review + contact / cover -->
<section class="sheet sheet--outside">
  <svg class="art" viewBox="0 0 720 509" xmlns="http://www.w3.org/2000/svg">
    <defs>
      <linearGradient id="floorScene" x1="0" y1="0" x2="1" y2="1">
        <stop offset="0" stop-color="#f3f4f6"/>
        <stop offset=".55" stop-color="#c9ced6"/>
        <stop offset="1" stop-color="#8fa2b8"/>
      </linearGradient>
      <linearGradient id="teamScene" x1="0" y1="0" x2="0" y2="1">
        <stop offset="0" stop-color="#e6e7ea"/>
        <stop offset=".5" stop-color="#b9c4cf"/>
        <stop offset="1" stop-color="#3a8fc6"/>
      </linearGradient>
      <radialGradient id="portraitScene">
        <stop offset="0" stop-color="#d8c7a4"/>
        <stop offset="1" stop-color="#a8c6de"/>
      </radialGradient>
    </defs>
    <g role="img" aria-label="Photo of a floor being vacuumed in a bright office lounge">
      <path d="M0,160 H222 V0 H472 C432,80 408,200 384,380 H0 Z" fill="url(#floorScene)"/>
    </g>
    <g role="img" aria-label="Photo of cleaning supplies: sprays, gloves and cloths">
      <path d="M472,0 H720 V380 H384 C408,200 432,80 472,0 Z" fill="url(#teamScene)"/>
    </g>
    <path d="M488,0 C446,84 420,200 398,340" fill="none" stroke="var(--green-light)" stroke-width="5"/>
    <g role="img" aria-label="Round inset photo of a cleaning bucket and cloths">
      <circle cx="404" cy="172" r="60" fill="url(#portraitScene)" stroke="var(--green-light)" stroke-width="4"/>
    </g>
    <path d="M300,318 C420,300 480,345 575,347 C645,348 690,325 720,305 V509 H300 Z" fill="var(--white)"/>
    <path d="M320,322 C430,318 480,362 575,365 C645,366 690,344 720,324" fill="none" stroke="var(--blue)" stroke-width="6"/>
    <path d="M0,340 C120,318 230,312 320,318 C420,325 470,380 570,382 C640,383 690,360 720,340 V509 H0 Z" fill="var(--green)"/>
    <circle cx="318" cy="330" r="47" fill="var(--white)" stroke="var(--blue)" stroke-width="4"/>
  </svg>

  <h2 class="heading" style="left:24px;top:30px"><span class="accent">Floor</span> <span class="main">Services</span></h2>
  <div class="copy" style="left:24px;top:62px">
    <p>Lorem Ipsum is simply dummy text of the printing and typesetting industry. Lorem Ipsum has been the industry's standard dummy text ever since the 1500s, when an unknown printer took a galley of type and scrambled it to make a type specimen book.</p>
    <p>Lorem Ipsum is simply dummy text of the printing and typesetting industry. Lorem Ipsum has been the industry's standard dummy text ever since the 1500s, when an unknown printer took a galley of type and scrambled it to make a type specimen book.</p>
  </div>

  <div class="brand brand--cover">BrightWave<small>Tristate</small></div>
  <div class="brand brand--badge">BrightWave<small>Tristate</small></div>

  <h3 class="review-title">Client Review</h3>
  <blockquote class="quote-box">
    <span class="mark">&ldquo;</span>
    Lorem Ipsum is simply dummy text of the printing and typesetting industry. Lorem Ipsum has been the industry's standard dummy text ever since the 1500s, when an unknown printer took a galley of type and scrambled it to make a type specimen book.
    <span class="by">Lorem Ipsum is simply</span>
  </blockquote>

  <h3 class="contact-title">Contact us</h3>
  <ul class="contact-list">
    <li><svg viewBox="0 0 10 10"><path d="M2 0.5 L3.6 2.6 L2.8 3.6 C3.5 5 4.9 6.4 6.4 7.2 L7.4 6.4 L9.5 8 L8.4 9.6 C4.5 9 1 5.5 0.4 1.6 Z"/></svg>555 018 2044</li>
    <li><svg viewBox="0 0 10 10"><path d="M0 2 H10 V8 H0 Z M0.8 2.6 L5 5.6 L9.2 2.6" /></svg>hello@brightwavetristate.com</li>
    <li><svg viewBox="0 0 10 10"><circle cx="5" cy="5" r="4.5"/></svg>www.brightwavetristate.com</li>
  </ul>

  <h1 class="cover-title">Commercial<br>Cleaning Services</h1>
  <p class="cover-url">www.brightwavetristate.com</p>
</section>

<!-- Inside spread: three services -->
<section class="sheet sheet--inside">
  <svg class="art" viewBox="0 0 720 509" xmlns="http://www.w3.org/2000/svg">
    <defs>
      <linearGradient id="officeScene" x1="0" y1="0" x2="1" y2="1">
        <stop offset="0" stop-color="#eef1f4"/><stop offset="1" stop-color="#9eabba"/>
      </linearGradient>
      <linearGradient id="covidScene" x1="0" y1="0" x2="1" y2="1">
        <stop offset="0" stop-color="#f6f7f8"/><stop offset="1" stop-color="#c7ccd3"/>
      </linearGradient>
      <linearGradient id="janitorScene" x1="0" y1="0" x2="0" y2="1">
        <stop offset="0" stop-color="#e8c99a"/><stop offset=".6" stop-color="#f2d23c"/><stop offset="1" stop-color="#b9a48a"/>
      </linearGradient>
    </defs>
    <g role="img" aria-label="Photo of office desks being cleaned"><rect x="0" y="0" width="242" height="290" fill="url(#officeScene)"/></g>
    <g role="img" aria-label="Photo of a disinfection sprayer over a work surface"><rect x="242" y="0" width="238" height="290" fill="url(#covidScene)"/></g>
    <g role="img" aria-label="Photo of a yellow mop bucket and caution sign"><rect x="480" y="0" width="240" height="290" fill="url(#janitorScene)"/></g>
    <path d="M0,262 C120,250 230,238 320,250 C400,262 450,286 520,280 C600,274 670,258 720,260 V509 H0 Z" fill="var(--white)"/>
    <path d="M0,262 C120,248 230,236 320,248 C400,260 450,284 520,278 C600,272 670,256 720,258" fill="none" stroke="var(--blue)" stroke-width="6"/>
  </svg>

  <h2 class="heading" style="left:25px;top:286px"><span class="accent">Office</span> <span class="main">Cleaning</span></h2>
  <div class="copy" style="left:25px;top:318px">
    <p>Lorem Ipsum is simply dummy text of the printing and typesetting industry. Lorem Ipsum has been the industry's standard dummy text ever since the 1500s, when an unknown printer took a galley of type and scrambled it to make a type specimen book.</p>
    <p>Lorem Ipsum is simply dummy text of the printing and typesetting industry. Lorem Ipsum has been the industry's standard dummy text ever since the 1500s, when an unknown printer took a galley of type and scrambled it to make a type specimen book.</p>
    <p>Lorem Ipsum is simply dummy text of the printing and typesetting industry. Lorem Ipsum has been the industry's standard dummy text ever since the 1500s, when an unknown printer took a galley of type and scrambled it to make a type specimen book.</p>
  </div>

  <h2 class="heading" style="left:263px;top:286px"><span class="accent">Covid</span> <span class="main">Cleaning</span></h2>
  <div class="copy" style="left:263px;top:318px">
    <p>Lorem Ipsum is simply dummy text of the printing and typesetting industry. Lorem Ipsum has been the industry's standard dummy text ever since the 1500s, when an unknown printer took a galley of type and scrambled it to make a type specimen book.</p>
    <p>Lorem Ipsum is simply dummy text of the printing and typesetting industry. Lorem Ipsum has been the industry's standard dummy text ever since the 1500s, when an unknown printer took a galley of type and scrambled it to make a type specimen book.</p>
    <p>Lorem Ipsum is simply dummy text of the printing and typesetting industry. Lorem Ipsum has been the industry's standard dummy text ever since the 1500s, when an unknown printer took a galley of type and scrambled it to make a type specimen book.</p>
  </div>

  <h2 class="heading" style="left:502px;top:292px"><span class="accent">Janitorial</span> <span class="main">Cleaning</span></h2>
  <div class="copy" style="left:502px;top:324px">
    <p>Lorem Ipsum is simply dummy text of the printing and typesetting industry. Lorem Ipsum has been the industry's standard dummy text ever since the 1500s, when an unknown printer took a galley of type and scrambled it to make a type specimen book.</p>
    <p>Lorem Ipsum is simply dummy text of the printing and typesetting industry. Lorem Ipsum has been the industry's standard dummy text ever since the 1500s, when an unknown printer took a galley of type and scrambled it to make a type specimen book.</p>
    <p>Lorem Ipsum is simply dummy text of the printing and typesetting industry. Lorem Ipsum has been the industry's standard dummy text ever since the 1500s, when an unknown printer took a galley of type and scrambled it to make a type specimen book.</p>
  </div>
</section>

</body>
</html>
```